Web Design for Independent Pet Supply shop.

Larkfield Critter Depot is a locally owned and operated premium natural pet food store and supply company with 2 thriving retail stores in Bend, Oregon, and a home delivery service. The pet food offered is the best on the market and may be described as “holistic”. Also on offer is a vast selection of toys, training tools, treats, and other supplies, as well as dog washing services that range from "do-it yourself" to "spa." Current site: LarkfieldCritterDepot.com. They need a new, updated and responsive site.
Likes:
Tovmira.com: Natural colors, not loud, pages in motion, simple & clean but very informative.
Dunmoregale.com: Everything in simple big colorful blocks. The specials run across the top and in motion. This site looks very professional but simple. The information is available several different places.
Quillbarrow.com: Again big blocks through out. Very Fun and inviting. Tons of information with videos and recipes and testimonials. Pleasant feel and colors as well.
Dislikes:
Zinvor.com: Looks cheap, hate the colors, very busy and over whelming. Hate the old style header bar going across with options. Too many printed words instead of fun images.
Colors should be "natural" tones, warm and soothing. Deep dark blue and greys with earthy wood color.
Do Not Use: Blue violet, violet, red violet

```html
<!DOCTYPE html>
<html lang="en">
<head>
<meta charset="utf-8">
<title>Larkfield Critter Depot</title>
<link href="https://fonts.googleapis.com/css2?family=Days+One&family=Open+Sans:wght@400;600;700&family=Dancing+Script:wght@700&display=swap" rel="stylesheet">
<style>
:root{
  --brown:#6a381c;
  --brown-dark:#4e2912;
  --green:#5f7e3b;
  --green-dark:#4b672c;
  --beige:#ebe3cb;
  --beige-light:#f2ecd9;
  --tan:#8b7e69;
  --ink:#3b2f27;
  --muted:#6b6155;
  --white:#ffffff;
  --gold:#e0b15a;
}
*{margin:0;padding:0;box-sizing:border-box}
html,body{width:1200px;height:5357px;overflow:hidden}
body{position:relative;background:var(--beige);font-family:"Open Sans",Arial,sans-serif;color:var(--ink)}
.abs{position:absolute}
.photo{position:absolute}
p{line-height:1.6}

/* hero */
.hero{left:0;top:0;width:1200px;height:750px;background:linear-gradient(180deg,#3f5a2a 0%,#6e8a45 38%,#a5a45c 62%,#7f9a48 100%)}
.hero-shade{left:0;top:0;width:1200px;height:200px;background:linear-gradient(180deg,rgba(0,0,0,.45),rgba(0,0,0,0))}
.brand{left:71px;top:66px;display:flex;align-items:center;gap:12px;color:var(--white);font-family:"Days One",sans-serif;font-size:26px;text-transform:uppercase}
.brand-dot{width:22px;height:22px;border-radius:50%;background:var(--white)}
.nav{left:905px;top:22px;width:270px;display:grid;grid-template-columns:1fr 1fr;column-gap:20px;font-size:14px;color:var(--white)}
.nav a{color:var(--white);text-decoration:none;display:block;padding:4px 0;border-bottom:1px solid rgba(255,255,255,.45)}
.hero-frame{left:346px;top:303px;width:511px;height:287px;border:3px solid rgba(255,255,255,.9);text-align:center}
.ribbon{position:absolute;left:40px;top:26px;width:425px;height:44px;background:var(--white);color:var(--brown);font-size:17px;font-weight:600;letter-spacing:2px;line-height:44px;text-transform:uppercase}
.hero-for{position:absolute;left:0;width:100%;top:82px;font-family:"Dancing Script",cursive;font-size:62px;color:var(--gold)}
.hero-title{position:absolute;left:0;width:100%;top:168px;font-family:"Open Sans",sans-serif;font-weight:700;font-size:56px;color:var(--white);text-transform:uppercase}
.social{left:936px;top:680px;display:flex;gap:10px}
.social span{width:40px;height:40px;border-radius:50%;border:2px solid var(--white)}

/* welcome */
.welcome{left:71px;top:703px;width:607px;height:404px;background:var(--brown);color:var(--white);text-align:center}
.welcome h1{position:absolute;left:0;top:80px;width:100%;font-family:"Days One",sans-serif;font-weight:400;font-size:31px;line-height:1.35;text-transform:uppercase}
.welcome-cta{position:absolute;left:0;top:186px;width:365px;text-align:center}
.welcome .link{display:block;font-size:14px;letter-spacing:1px;text-transform:uppercase}
.welcome .mark{width:40px;height:40px;border-radius:50%;background:var(--white);margin:26px auto 0}
.store-photo{left:436px;top:875px;width:689px;height:446px;background:linear-gradient(135deg,#c9a66a,#5d7b8a 45%,#6a8c4c 75%,#3b3a33)}
.intro{left:96px;top:1150px;width:320px;padding-left:18px;border-left:2px solid var(--muted);font-size:15px;color:var(--muted)}

/* connectors */
.vline{position:absolute;width:2px;background:var(--ink)}
.dot{position:absolute;width:10px;height:10px;border-radius:50%;background:var(--ink)}

/* section headings */
.sec-title{font-family:"Days One",sans-serif;color:var(--brown);text-transform:uppercase;line-height:1}
.sec-sub{font-size:13px;font-weight:600;text-transform:uppercase;color:var(--ink);letter-spacing:.5px}

/* dog wash */
.wash-photo{left:0;top:1493px;width:1200px;height:642px;background:linear-gradient(90deg,#2b2a26 0%,#5a5246 35%,#b99a7c 55%,#d0c4b0 72%,#8a9a7a 100%)}
.wash-box{left:679px;top:1850px;width:449px;height:285px;background:var(--green);color:var(--white);padding:22px 26px;font-size:13.5px}

/* products */
.prod-lead{left:436px;top:2178px;width:692px;text-align:right;font-size:14px;color:var(--muted)}
.kibble{left:436px;top:2285px;width:692px;height:429px;background:linear-gradient(160deg,#3f4d2c,#7a5230 45%,#d9d4c8 70%,#b9b3a5)}
.soup{left:164px;top:2457px;width:422px;height:421px;background:linear-gradient(135deg,#5a3b1f,#e6a043 45%,#f2e6cf 65%,#7c5a38);border:6px solid var(--beige-light)}
.prod-text{left:636px;top:2785px;width:330px;font-size:14px;color:var(--muted)}
.small-dog{left:936px;top:2821px;width:225px;height:357px;background:radial-gradient(ellipse at 50% 55%,#4a3526 0%,#7a5a3e 40%,rgba(235,227,203,0) 70%)}
.treats{left:0;top:3035px;width:1200px;height:679px;background:linear-gradient(180deg,#d8cfc0 0%,#a8662f 40%,#7d4520 70%,#3d3a36 100%)}
.caption{left:164px;top:3700px;width:872px;height:121px;background:var(--brown);color:var(--white);text-align:center;padding:18px 40px}
.caption h3{font-size:16px;font-weight:700;text-transform:uppercase;letter-spacing:.5px}
.caption p{font-size:13.5px;margin-top:6px}
.arrow-btn{position:absolute;top:3700px;width:107px;height:121px;background:var(--green);display:flex;align-items:center;justify-content:center}

/* tiles */
.tile{position:absolute;width:332px;overflow:hidden}
.tile .img{position:absolute;left:0;top:0;width:100%;height:100%}
.tile .bar{position:absolute;left:0;bottom:0;width:100%;height:52px;background:rgba(106,56,28,.92);color:var(--white);display:flex;align-items:center;justify-content:space-between;padding:0 16px;font-size:18px;font-weight:700;text-transform:uppercase}
.tile .bar.light{background:rgba(60,56,50,.8)}
.go{width:26px;height:26px;border-radius:50%;border:2px solid var(--white);display:flex;align-items:center;justify-content:center}
.news{left:436px;top:3928px;width:332px;height:679px;background:var(--tan);color:var(--white);padding:26px 24px}
.news h3{font-size:17px;font-weight:700;text-transform:uppercase;text-align:center;line-height:1.35}
.news .img{width:284px;height:232px;margin:22px 0;background:linear-gradient(135deg,#3a3430,#7f6a5c 50%,#c7b9a8)}
.news p{font-size:13px}

/* contact */
.store-info{font-size:14px;color:var(--ink);line-height:1.55}
.store-info h4{color:var(--brown);font-size:15px;font-weight:700;text-transform:uppercase;margin-bottom:16px}
.store-info .hours{color:var(--green);font-family:"Days One",sans-serif;font-size:17px;text-transform:uppercase;margin:18px 0 6px}
.map{left:0;top:4946px;width:1200px;height:368px;background:linear-gradient(135deg,#e4e1d8,#d5d9cc 40%,#e9e6dc 70%,#cfd6c6);border-top:4px solid var(--brown)}
.footer{left:0;top:5314px;width:1200px;height:43px;background:var(--beige-light);font-size:11px;color:var(--muted);padding:14px 71px}
.contact-btn{left:1000px;top:5314px;width:200px;height:43px;background:var(--green);color:var(--white);font-weight:700;font-size:15px;text-transform:uppercase;text-align:center;line-height:43px}
</style>
</head>
<body>

<!-- hero -->
<div class="photo hero abs" role="img" aria-label="Golden retriever running across a sunny lawn"></div>
<div class="hero-shade abs"></div>
<div class="brand abs"><span class="brand-dot"></span>Larkfield Critter Depot</div>
<nav class="nav abs">
  <div><a>Home</a><a>Events</a><a>Blog</a><a>About</a><a>Dog Wash</a></div>
  <div><a>Products</a><a>Resources</a><a>Links</a><a>Testimonials</a><a>Contact</a></div>
</nav>
<div class="hero-frame abs">
  <div class="ribbon">Dedicated to a better diet</div>
  <div class="hero-for">For</div>
  <div class="hero-title">A Healthier Pet</div>
</div>
<div class="social abs"><span></span><span></span><span></span><span></span></div>

<!-- welcome -->
<section class="welcome abs">
  <h1>Welcome to<br>Larkfield Critter Depot!</h1>
  <div class="welcome-cta">
    <span class="link">Visit our store</span>
    <div class="mark"></div>
  </div>
</section>
<div class="photo store-photo" role="img" aria-label="Inside the store, aisles stocked with pet food bags"></div>
<p class="intro abs">We are a locally owned and operated premium natural pet food store and supply company. The whole idea for Larkfield Critter Depot started back in 1990 when Mara Ellison's (owner) dog became sick due to a food allergy.</p>

<div class="vline" style="left:777px;top:1321px;height:70px"></div>
<div class="dot" style="left:773px;top:1386px"></div>
<div class="abs" style="left:600px;top:1402px;width:356px;text-align:center">
  <div class="sec-title" style="font-size:40px">Dog Wash</div>
  <div class="sec-sub" style="margin-top:8px">See dog wash services</div>
</div>
<div class="vline" style="left:777px;top:1470px;height:23px"></div>

<!-- dog wash -->
<div class="photo wash-photo" role="img" aria-label="Dog being rinsed with a shower head at the wash station"></div>
<div class="wash-box abs"><p>At Larkfield Critter Depot we offer large, professional stainless steel bathing tubs, temperature controlled bathing water, a large variety of shampoos and conditioners, powerful professional forced air dryers, towels, aprons, and all of the tools and supplies you will need to give you and your dog the best, most relaxing, and fun bath experience. We have options for every four-legged friend that cover three main categories, the "You Wash", "We Wash", and our Mud Baths!</p></div>

<!-- products -->
<p class="prod-lead abs">Lorem ipsum dolor sit amet, consectetuer adipiscing elit, sed diam nonummy nibh euismod<br>tincidunt ut laoreet dolore magna aliquam erat volutpat. Ut wisi enim ...</p>
<div class="abs" style="left:71px;top:2221px">
  <div class="sec-title" style="font-size:52px;line-height:.95">Our<br>Products</div>
  <div class="sec-sub" style="margin-top:10px">See our dog products store</div>
</div>
<div class="vline" style="left:230px;top:2378px;height:79px"></div>
<div class="photo kibble" role="img" aria-label="Bowl filled with dry dog kibble"></div>
<div class="photo soup" role="img" aria-label="Bowl of chicken and vegetable stew"></div>
<div class="vline" style="left:374px;top:2884px;height:140px"></div>
<div class="dot" style="left:370px;top:3020px"></div>
<p class="prod-text abs">Lorem ipsum dolor sit amet, consectetuer adipiscing elit, sed diam nonummy nibh euismod tincidunt ut laoreet dolore magna aliquam erat volutpat. Lorem ipsum dolor sit amet, consectetuer adipiscing elit, sed diam nonummy nibh euismod tincidunt ut laoreet dolore magna aliquam erat volutpat. Ut wisi enim ...</p>
<div class="photo small-dog" role="img" aria-label="Small short-haired dog standing"></div>
<div class="photo treats" role="img" aria-label="Bowl of baked dog biscuit treats"></div>
<div class="arrow-btn" style="left:0">
  <svg width="34" height="34" viewBox="0 0 34 34"><circle cx="17" cy="17" r="15" fill="none" stroke="#fff" stroke-width="2"/><path d="M20 10 13 17l7 7" fill="none" stroke="#fff" stroke-width="2.5"/></svg>
</div>
<div class="caption abs">
  <h3>Lorem ipsum dolor sit consectetur adipiscing elit</h3>
  <p>Lorem ipsum dolor sit amet, consectetuer adipiscing elit, sed diam nonummy nibh euismod tincidunt ut laoreet dolore magna aliquam erat volutpat. Ut wisi enim ...</p>
</div>
<div class="arrow-btn" style="left:1093px">
  <svg width="34" height="34" viewBox="0 0 34 34"><circle cx="17" cy="17" r="15" fill="none" stroke="#fff" stroke-width="2"/><path d="M14 10l7 7-7 7" fill="none" stroke="#fff" stroke-width="2.5"/></svg>
</div>

<!-- news & services -->
<div class="tile" style="left:71px;top:3928px;height:197px">
  <div class="img" role="img" aria-label="People at a store tasting event" style="background:linear-gradient(135deg,#5b6a78,#a58a6e 55%,#d9c6a6)"></div>
  <div class="bar"><span>Mutt Brew</span><span class="go"><svg width="10" height="12" viewBox="0 0 10 12"><path d="M2 1l6 5-6 5" fill="none" stroke="#fff" stroke-width="2"/></svg></span></div>
</div>
<div class="tile" style="left:71px;top:4160px;height:197px">
  <div class="img" role="img" aria-label="Golden dog lying on grass" style="background:linear-gradient(135deg,#6f8a3e,#c59a52 55%,#8c6b3a)"></div>
  <div class="bar"><span>Kelvane Lawsuit</span><span class="go"><svg width="10" height="12" viewBox="0 0 10 12"><path d="M2 1l6 5-6 5" fill="none" stroke="#fff" stroke-width="2"/></svg></span></div>
</div>
<div class="tile" style="left:71px;top:4385px;height:204px">
  <div class="img" role="img" aria-label="Shelves of pet food bags on sale" style="background:linear-gradient(135deg,#4e7a8a,#8fae6a 50%,#d2c48a)"></div>
  <div class="bar"><span>Sale</span><span class="go"><svg width="10" height="12" viewBox="0 0 10 12"><path d="M2 1l6 5-6 5" fill="none" stroke="#fff" stroke-width="2"/></svg></span></div>
</div>

<section class="news abs">
  <h3>The Larkfield Critter Depot Dog Wash News and Updates</h3>
  <div class="img" role="img" aria-label="Dog paws resting on a towel"></div>
  <p>The Larkfield Critter Depot Dog Wash attendants are always here to help wash your four-legged friends, and trim their nails... but they are also here to help educate all of our Nail Trim customers on why it is an essential routine for our pups, especially if they don't run and walk as much as they would in the wild.</p>
</section>

<div class="abs" style="left:803px;top:3910px;width:322px;text-align:right">
  <div class="sec-title" style="font-size:52px;line-height:.95">Pet<br>Services</div>
  <div class="sec-sub" style="margin-top:10px">See all other services</div>
</div>
<div class="vline" style="left:1000px;top:4075px;height:67px"></div>
<div class="tile" style="left:793px;top:4142px;height:197px">
  <div class="img" role="img" aria-label="Community outreach banner with dark background" style="background:linear-gradient(135deg,#2e2d2a,#4a4a42 60%,#6c6a5e)"></div>
  <div class="bar light"><span>Hope Community</span><span class="go"><svg width="10" height="12" viewBox="0 0 10 12"><path d="M2 1l6 5-6 5" fill="none" stroke="#fff" stroke-width="2"/></svg></span></div>
</div>
<div class="tile" style="left:793px;top:4385px;height:204px">
  <div class="img" role="img" aria-label="Dog portrait on a neutral backdrop" style="background:linear-gradient(135deg,#d8cdb8,#9a6a44 50%,#e2d8c4)"></div>
  <div class="bar"><span>Snapfeed</span><span class="go"><svg width="10" height="12" viewBox="0 0 10 12"><path d="M2 1l6 5-6 5" fill="none" stroke="#fff" stroke-width="2"/></svg></span></div>
</div>

<!-- contact -->
<div class="store-info abs" style="left:71px;top:4640px;width:330px">
  <h4>Larkfield Critter Depot – East</h4>
  <div>418 NE Alder Crest Dr<br>Larkfield, WA 98312</div>
  <div style="margin-top:12px">360-555-0142<br>eastside@larkfieldcritterdepot.com</div>
  <div class="hours">Operating Hours:</div>
  <div>Every day 8:30 a.m. – 7 p.m.<br>Dog Wash 8:30 a.m. – 6 p.m.</div>
</div>
<div class="vline" style="left:599px;top:4607px;height:60px"></div>
<div class="abs" style="left:440px;top:4680px;width:320px;text-align:center">
  <div class="sec-title" style="font-size:56px;line-height:.95">Get in<br>Touch</div>
  <div class="sec-sub" style="margin-top:10px">Our contact details</div>
</div>
<div class="vline" style="left:599px;top:4840px;height:106px"></div>
<div class="dot" style="left:595px;top:4936px"></div>
<div class="store-info abs" style="left:813px;top:4640px;width:330px;text-align:right">
  <h4>Larkfield Critter Depot – West</h4>
  <div>127 SW Juniper Loop<br>Larkfield, WA 98315</div>
  <div style="margin-top:12px">360-555-0187<br>westside@larkfieldcritterdepot.com</div>
  <div class="hours">Operating Hours:</div>
  <div>Mon – Sat 8 a.m. – 7 p.m.<br>Sunday 11 a.m. – 5 p.m.</div>
</div>

<div class="photo map abs" role="img" aria-label="Street map showing the store location"></div>
<footer class="footer abs">Copyright 2015 Larkfield Critter Depot. All Rights Reserved &nbsp;|&nbsp; Returns Policy &nbsp;|&nbsp; Privacy Policy &nbsp;|&nbsp; Employment &nbsp;|&nbsp; Staff Login</footer>
<div class="contact-btn abs">Contact Us</div>

</body>
</html>
```